Sports Therapy and Personal Training

I need a business card design for a new business based in Toronto called "Vellmore Athletics" I am a sports therapist as well as a strength and conditioning coach, therefore I work mainly with high level athletes and physically active people. I am starting my own therapy/training business. The services I will be offering include fitness consultation, personal training, athlete assessments, and rehabilitation therapy. These services will be delivered in peoples homes and/or a facility in which I rent space.

The final design should communicate "high-end" and "quality"

Target Market(s)

athletes and physically active people

Industry/Entity Type

Fitness

Requirements
Must have
• 1. The business logo - files attached

2. my name and credentials

Derek Vellmore - CAT(C), CK, CSCS,

Certified Athletic Therapist
Strength and Conditioning Specialist

3. website - www.vellmoreathletics.example

4. email address - derek@vellmoreathletics.example

5. phone number

```html
<!DOCTYPE html>
<html lang="en">
<head>
<meta charset="utf-8">
<title>Vellmore Athletics – Business Card</title>
<link rel="stylesheet" href="https://fonts.googleapis.com/css2?family=Exo+2:wght@300;400;600&family=Open+Sans:wght@400&display=swap">
<style>
  :root {
    --page: #ffffff;
    --card-edge: #a9a9a9;
    --card-front-light: #f7f7f7;
    --card-front-mid: #e2e2e2;
    --card-back-light: #e9e9e9;
    --card-back-mid: #c4c4c4;
    --inner-rule: #b3b3b3;
    --ink-dark: #3b3b3b;
    --ink-mid: #555555;
    --accent-red: #e2321f;
    --label-ink: #111111;
  }
  html, body {
    margin: 0;
    padding: 0;
    width: 1200px;
    height: 509px;
    overflow: hidden;
    background: var(--page);
  }
  .sheet {
    position: relative;
    width: 1200px;
    height: 509px;
  }
  .card {
    position: absolute;
    top: 73px;
    width: 570px;
    height: 323px;
    box-sizing: border-box;
    border: 1px solid var(--card-edge);
  }
  .card-front {
    left: 26px;
    background: radial-gradient(ellipse at 25% 30%, var(--card-front-light) 0%, var(--card-front-mid) 90%);
  }
  .card-back {
    left: 611px;
    width: 564px;
    background:
      radial-gradient(ellipse at 55% 30%, rgba(255,255,255,0.65) 0%, rgba(255,255,255,0) 45%),
      linear-gradient(180deg, var(--card-back-light) 0%, var(--card-back-mid) 100%);
  }
  .card-frame {
    position: absolute;
    inset: 13px;
    border: 1px solid var(--inner-rule);
  }
  .brand-name {
    font-family: "Exo 2", sans-serif;
    font-weight: 600;
    color: var(--ink-dark);
    letter-spacing: 0.5px;
    display: flex;
    align-items: center;
    gap: 12px;
    white-space: nowrap;
  }
  .brand-square {
    width: 18px;
    height: 18px;
    background: var(--accent-red);
    flex: none;
  }
  .front-brand {
    position: absolute;
    left: 0;
    right: 0;
    top: 143px;
    justify-content: center;
    font-size: 32px;
  }
  .back-brand {
    position: absolute;
    left: 30px;
    top: 30px;
    font-size: 24px;
  }
  .back-brand .brand-square {
    width: 30px;
    height: 30px;
  }
  .header-rule {
    position: absolute;
    left: 34px;
    right: 14px;
    top: 82px;
    height: 1px;
    background: var(--inner-rule);
  }
  .contact-block {
    position: absolute;
    right: 28px;
    top: 140px;
    text-align: right;
    font-family: "Exo 2", sans-serif;
    font-weight: 300;
  }
  .holder-name {
    font-size: 23px;
    color: var(--ink-mid);
    margin: 0 0 4px;
  }
  .holder-role {
    font-size: 16px;
    color: var(--accent-red);
    margin: 0 10px 3px 0;
  }
  .website {
    font-size: 22px;
    color: var(--ink-mid);
    margin: 4px 0 0;
  }
  .footer-line {
    position: absolute;
    left: 27px;
    right: 22px;
    top: 282px;
    display: flex;
    justify-content: space-between;
    font-family: "Exo 2", sans-serif;
    font-weight: 300;
    font-size: 14px;
    color: var(--ink-mid);
  }
  .side-label {
    position: absolute;
    top: 402px;
    font-family: "Open Sans", sans-serif;
    font-size: 38px;
    color: var(--label-ink);
    text-align: center;
  }
  .label-front { left: 26px; width: 570px; }
  .label-back { left: 611px; width: 564px; }
</style>
</head>
<body>
<main class="sheet">
  <section class="card card-front" aria-label="Card front">
    <div class="card-frame"></div>
    <div class="brand-name front-brand"><span class="brand-square"></span>Vellmore Athletics</div>
  </section>

  <section class="card card-back" aria-label="Card back">
    <div class="card-frame"></div>
    <div class="brand-name back-brand"><span class="brand-square"></span>Vellmore Athletics</div>
    <div class="header-rule"></div>
    <div class="contact-block">
      <p class="holder-name">Derek Vellmore - CAT(C), CK, CSCS,</p>
      <p class="holder-role">Certified Athletic Therapist</p>
      <p class="holder-role">Strength and Conditioning Specialist</p>
      <p class="website">www.vellmoreathletics.example</p>
    </div>
    <div class="footer-line">
      <span class="email">derek@vellmoreathletics.example</span>
      <span class="phone">phone:00158276</span>
    </div>
  </section>

  <div class="side-label label-front">front</div>
  <div class="side-label label-back">back</div>
</main>
</body>
</html>
```